Business Card and stationary project for Nutrition Consulitng Company
QV Nutrition Consulting, PC
Business Card and stationary project for Nutrition Consulitng Company - Health
Creative Brief
Bright & Fun-filled
leave adjustable for each staff
5182 27th Ave. Suite 100 Columbus, NE 68457
leave adjustable
rmalden@qvnutritionconsulting.example
www.qvnutritionconsulting.example
I would like the business cards to be editable for each staff member. This would include name, title, (402) 555-0173, and email address.
please address my website www.qvnutriitionconsulting.example for ideas, as well as the uploaded logo and letter head

```html
<!DOCTYPE html>
<html lang="en">
<head>
<meta charset="utf-8">
<title>QV Nutrition Consulting, PC — Stationery</title>
<link rel="stylesheet" href="https://fonts.googleapis.com/css2?family=Montserrat:wght@700&family=Open+Sans:wght@400;600&display=swap">
<style>
  :root {
    --brown: #6b3a22;
    --brown-dark: #552c18;
    --orange: #f07d1a;
    --green: #8dc63f;
    --red: #d9312b;
    --paper: #ffffff;
    --ink: #5e5e5e;
    --ground: #e8e5e1;
    --rule: #d6d1cc;
  }
  * { box-sizing: border-box; margin: 0; padding: 0; }
  html, body { width: 1200px; height: 434px; overflow: hidden; background: var(--ground); }
  body { position: relative; font-family: "Open Sans", Arial, sans-serif; color: var(--ink); }

  .sheet { position: absolute; background: var(--paper); box-shadow: 0 2px 6px rgba(0,0,0,.18); overflow: hidden; }

  .brand { display: flex; align-items: center; gap: 5px; font-family: "Montserrat", Arial, sans-serif; font-weight: 700; color: var(--brown); white-space: nowrap; }
  .brand .dot { width: 10px; height: 10px; border-radius: 50%; background: var(--orange); flex: none; }
  .brand.on-dark { color: #fff; }

  .rule { position: absolute; height: 2px; background: var(--orange); }
  .small { font-size: 6.5px; line-height: 1.55; }

  /* Decorative artwork area: soft gradient placeholder */
  .art-area { position: absolute; background: linear-gradient(135deg, rgba(141,198,63,.55), rgba(240,125,26,.55) 55%, rgba(217,49,43,.45)); }
  .art-area.faint { background: linear-gradient(135deg, #f3f3f3, #e2e2e2); }

  /* Letterhead */
  .letterhead { left: 20px; top: 28px; width: 222px; height: 380px; }
  .letterhead .brand { position: absolute; left: 18px; top: 22px; font-size: 11px; }
  .letterhead .rule { left: 18px; right: 18px; top: 46px; }
  .letterhead .band { position: absolute; left: 0; bottom: 0; width: 100%; height: 58px; }
  .letterhead .address { position: absolute; left: 18px; bottom: 66px; }

  /* Business card front */
  .card-front { left: 262px; top: 34px; width: 240px; height: 138px; }
  .card-front .brand { position: absolute; left: 14px; top: 14px; font-size: 10px; }
  .card-front .rule { left: 14px; width: 150px; top: 34px; }
  .card-front .person { position: absolute; left: 14px; top: 46px; }
  .card-front .person .name { font-size: 9px; font-weight: 600; color: var(--brown); }
  .card-front .contact { position: absolute; left: 14px; bottom: 12px; }
  .card-front .edge { position: absolute; right: 0; top: 0; height: 100%; width: 40px; }

  /* Business card back */
  .card-back { left: 262px; top: 190px; width: 240px; height: 138px; background: var(--brown); }
  .card-back .brand { position: absolute; right: 14px; top: 16px; font-size: 10px; }
  .card-back .art-area { left: 0; bottom: 0; width: 70px; height: 74px; }
  .card-back .web { position: absolute; right: 14px; bottom: 14px; color: #fff; }

  /* Envelope */
  .envelope { left: 522px; top: 28px; width: 300px; height: 140px; }
  .envelope .brand { position: absolute; left: 14px; top: 14px; font-size: 10px; }
  .envelope .rule { left: 14px; width: 140px; top: 34px; }
  .envelope .address { position: absolute; left: 14px; top: 42px; }
  .envelope .band { position: absolute; left: 0; bottom: 0; width: 100%; height: 26px; background: var(--brown); }
  .envelope .web { position: absolute; right: 14px; bottom: 8px; color: #fff; }

  /* Fax sheet */
  .fax { left: 522px; top: 186px; width: 150px; height: 222px; }
  .fax .title { position: absolute; left: 12px; top: 14px; font-family: "Montserrat", Arial, sans-serif; font-weight: 700; font-size: 10px; color: var(--brown); }
  .fax .rule { left: 12px; right: 12px; top: 30px; }
  .fax .fields { position: absolute; left: 12px; right: 12px; top: 40px; list-style: none; }
  .fax .fields li { font-size: 7px; border-bottom: 1px solid var(--rule); padding: 6px 0 3px; }
  .fax .brand { position: absolute; left: 12px; bottom: 14px; font-size: 8px; }

  /* Compliment slip */
  .slip { left: 690px; top: 186px; width: 132px; height: 222px; }
  .slip .brand { position: absolute; left: 10px; right: 10px; top: 12px; font-size: 7.5px; white-space: normal; line-height: 1.25; align-items: flex-start; }
  .slip .brand .dot { margin-top: 1px; }
  .slip .rule { left: 10px; right: 10px; top: 36px; }
  .slip .address { position: absolute; left: 10px; bottom: 40px; }
  .slip .band { position: absolute; left: 0; bottom: 0; width: 100%; height: 26px; background: var(--brown); }

  /* Presentation folder */
  .folder { left: 842px; top: 14px; width: 340px; height: 404px; background: transparent; box-shadow: none; }
  .folder .cover { position: absolute; left: 0; top: 0; width: 170px; height: 100%; background: var(--brown); overflow: hidden; }
  .folder .inside { position: absolute; left: 170px; top: 0; width: 170px; height: 100%; background: var(--paper); overflow: hidden; }
  .folder .cover .brand { position: absolute; left: 14px; top: 22px; font-size: 8.5px; }
  .folder .cover .rule { left: 14px; right: 14px; top: 42px; }
  .folder .cover .art-area { right: 0; top: 80px; width: 100px; height: 130px; }
  .folder .cover .address { position: absolute; left: 14px; bottom: 20px; color: #fff; }
  .folder .inside .art-area { right: 0; top: 20px; width: 120px; height: 150px; }
  .folder .pocket { position: absolute; left: 0; bottom: 0; width: 100%; height: 130px; background: var(--brown-dark); }
  .folder .pocket .slot { position: absolute; left: 30px; top: 18px; width: 110px; height: 64px; background: var(--paper); box-shadow: 0 1px 3px rgba(0,0,0,.3); }
  .folder .pocket .slot .brand { position: absolute; left: 8px; top: 8px; font-size: 6px; }
  .folder .pocket .slot .dot { width: 6px; height: 6px; }
  .folder .pocket .slot .small { position: absolute; left: 8px; bottom: 6px; font-size: 4.5px; }
</style>
</head>
<body>

<section class="sheet letterhead">
  <div class="brand"><span class="dot"></span>QV Nutrition Consulting, PC</div>
  <div class="rule"></div>
  <p class="address small">5182 27th Ave. Suite 100<br>Columbus, NE 68457<br>Phone (402) 555-0148 · Fax (402) 555-0149<br>www.qvnutritionconsulting.example</p>
  <svg class="band" viewBox="0 0 222 58" preserveAspectRatio="none" aria-hidden="true">
    <path d="M0 58 L0 10 Q60 40 222 46 L222 58 Z" fill="var(--brown)"/>
    <path d="M0 10 Q60 40 222 46" fill="none" stroke="var(--orange)" stroke-width="2"/>
  </svg>
</section>

<section class="sheet card-front">
  <div class="brand"><span class="dot"></span>QV Nutrition Consulting, PC</div>
  <div class="rule"></div>
  <div class="person small">
    <div class="name">Staff Name</div>
    <div>Registered Dietitian</div>
  </div>
  <p class="contact small">5182 27th Ave. Suite 100, Columbus, NE 68457<br>Cell (402) 555-0173 · Office (402) 555-0148<br>rmalden@qvnutritionconsulting.example</p>
  <svg class="edge" viewBox="0 0 40 138" preserveAspectRatio="none" aria-hidden="true">
    <path d="M40 0 L22 0 Q0 69 22 138 L40 138 Z" fill="var(--brown)"/>
    <path d="M22 0 Q0 69 22 138" fill="none" stroke="var(--orange)" stroke-width="2"/>
  </svg>
</section>

<section class="sheet card-back">
  <div class="art-area" role="img" aria-label="Decorative artwork in green, orange and red"></div>
  <div class="brand on-dark"><span class="dot"></span>QV Nutrition Consulting, PC</div>
  <p class="web small">www.qvnutritionconsulting.example</p>
</section>

<section class="sheet envelope">
  <div class="brand"><span class="dot"></span>QV Nutrition Consulting, PC</div>
  <div class="rule"></div>
  <p class="address small">5182 27th Ave. Suite 100<br>Columbus, NE 68457</p>
  <div class="band"></div>
  <p class="web small">www.qvnutritionconsulting.example</p>
</section>

<section class="sheet fax">
  <h2 class="title">Fax Sheet</h2>
  <div class="rule"></div>
  <ul class="fields">
    <li>To:</li>
    <li>From:</li>
    <li>Fax:</li>
    <li>Date:</li>
    <li>Pages:</li>
    <li>Re:</li>
  </ul>
  <div class="brand"><span class="dot"></span>QV Nutrition Consulting, PC</div>
</section>

<section class="sheet slip">
  <div class="brand"><span class="dot"></span><span>QV Nutrition Consulting, PC</span></div>
  <div class="rule"></div>
  <p class="address small">5182 27th Ave. Suite 100<br>Columbus, NE 68457<br>(402) 555-0148</p>
  <div class="band"></div>
</section>

<section class="sheet folder">
  <div class="cover">
    <div class="brand on-dark"><span class="dot"></span>QV Nutrition Consulting, PC</div>
    <div class="rule"></div>
    <div class="art-area" role="img" aria-label="Decorative artwork in green, orange and red"></div>
    <p class="address small">5182 27th Ave. Suite 100<br>Columbus, NE 68457<br>www.qvnutriitionconsulting.example</p>
  </div>
  <div class="inside">
    <div class="art-area faint" role="img" aria-label="Faint grey decorative artwork"></div>
    <div class="pocket">
      <div class="slot">
        <div class="brand"><span class="dot"></span>QV Nutrition Consulting, PC</div>
        <p class="small">Staff Name · (402) 555-0173</p>
      </div>
    </div>
  </div>
</section>

</body>
</html>
```